Modern Lawfirm Business Card Design

We're looking for a business card to incorporate the newly created logo we had made.

Ideally looking for a law firm business card demonstrating, modern, minimalist, strong/bold design.

I'm open to any design honestly, but nothing "flashy".

Target Market(s)

Immigration law, family immigration, humanitarian, general legal

Industry/Entity Type

Law Firm

Contact Information for Business Card

Please use dummy information, name, street address, city, state, phone number, email, website.

Font styles to use
Serif
Sans Serif

Requirements
Must have
• Please use dummy information, name, street address, city, state, phone number, email, website.

```html
<!DOCTYPE html>
<html lang="en">
<head>
<meta charset="utf-8">
<title>Varela Immigration Law – Business Card</title>
<link href="https://fonts.googleapis.com/css2?family=Fira+Sans:wght@400;600&display=swap" rel="stylesheet">
<style>
  :root {
    --backdrop: #e3e4e6;
    --paper: #ffffff;
    --brand-blue: #0a55a8;
    --brand-blue-light: #4f86c6;
    --ink-white: #ffffff;
    --rule: rgba(255,255,255,0.55);
  }
  * { margin: 0; padding: 0; box-sizing: border-box; }
  html, body {
    width: 1200px; height: 1200px; overflow: hidden;
    background: var(--backdrop);
    font-family: "Fira Sans", Arial, sans-serif;
  }
  .sheet {
    position: relative; width: 1200px; height: 1200px;
    display: flex; flex-direction: column; align-items: center; justify-content: center; gap: 60px;
  }
  .card {
    position: relative; width: 840px; height: 480px;
    background: var(--paper);
    box-shadow: 0 6px 18px rgba(0,0,0,0.12);
    overflow: hidden;
  }
  .card-band { position: absolute; inset: 0; width: 100%; height: 100%; }
  .wordmark {
    position: absolute; display: flex; align-items: center; gap: 12px;
    color: var(--brand-blue); font-weight: 600; letter-spacing: 1px; white-space: nowrap;
  }
  .wordmark-square { width: 18px; height: 18px; background: var(--brand-blue); }
  .wordmark-text { font-size: 30px; text-transform: uppercase; }
  .front .wordmark { top: 58px; right: 60px; }
  .back .wordmark { top: 50%; left: 50%; transform: translate(-50%, -50%); }
  .back .wordmark-text { font-size: 36px; }
  .contact-list {
    position: absolute; left: 48px; top: 212px; list-style: none;
    color: var(--ink-white); font-size: 19px; line-height: 34px;
    padding-bottom: 14px; border-bottom: 1px solid var(--rule); width: 320px;
  }
  .contact-list li { display: flex; align-items: center; gap: 12px; white-space: nowrap; }
  .contact-list svg { width: 16px; height: 16px; fill: var(--ink-white); flex: none; }
  .holder {
    position: absolute; right: 60px; bottom: 110px; text-align: right; color: var(--ink-white);
  }
  .holder-name { font-size: 32px; font-weight: 600; letter-spacing: 0.5px; text-transform: uppercase; }
  .holder-title { font-size: 19px; margin-top: 2px; }
</style>
</head>
<body>
<main class="sheet">
  <section class="card front">
    <svg class="card-band" viewBox="0 0 840 480" preserveAspectRatio="none" aria-hidden="true">
      <polygon points="0,120 170,120 215,160 840,160 840,400 0,400" fill="var(--brand-blue)"/>
      <polygon points="215,160 840,160 840,176 236,176" fill="var(--brand-blue-light)" opacity="0.7"/>
      <polygon points="236,188 840,188 840,196 246,196" fill="var(--brand-blue-light)" opacity="0.45"/>
    </svg>
    <div class="wordmark"><span class="wordmark-square"></span><span class="wordmark-text">Varela Immigration Law</span></div>
    <ul class="contact-list">
      <li><svg viewBox="0 0 16 16"><path d="M3 1l3 3-2 2c1 2 3 4 5 5l2-2 3 3-2 3C6 15 1 10 0 4z"/></svg>1-555-208143</li>
      <li><svg viewBox="0 0 16 16"><circle cx="8" cy="8" r="7" fill="none" stroke="#fff" stroke-width="1.5"/><path d="M1 8h14M8 1v14" stroke="#fff" stroke-width="1.2"/></svg>www.varelalaw.com</li>
      <li><svg viewBox="0 0 16 16"><rect x="1" y="3" width="14" height="10"/><path d="M1 3l7 6 7-6" fill="none" stroke="#0a55a8" stroke-width="1.3"/></svg>mark@varelalaw.com</li>
      <li><svg viewBox="0 0 16 16"><path d="M8 1l7 7h-2v7H9v-4H7v4H3V8H1z"/></svg>Harbor City, Eastvale Land</li>
    </ul>
    <div class="holder">
      <p class="holder-name">Mark Ellison</p>
      <p class="holder-title">Director</p>
    </div>
  </section>
  <section class="card back">
    <div class="wordmark"><span class="wordmark-square"></span><span class="wordmark-text">Varela Immigration Law</span></div>
  </section>
</main>
</body>
</html>
```